Premium label design for product needed

UPDATE: (Scroll down)
For a face care product i need a new front label on the bottle. The current one is white and i want to add the franchise color green. The objective is to premiunize the packaging and to give guidance to the consumers to find their franchise color. The task is to find several option to color the label on the bottle in the most premium way. But at the same time it should not be playful, more in a serious medical direction or in a counterbrand direction. It should look absolutely premium. but should not shout to much. The text structure should remain the same. I will provide a powerpoint slide to illustrate the task even clearer.
UPDATE: DO NOT DESIGN THE FOLDING BOX, only design the bottle. The folding box only serves the purpose of giving the text/layout structure and rough color intent.

Target Market(s)

female 25-39

Requirements
Must have
• Premium, Uniqueness, Innovative

```html
<!DOCTYPE html>
<html lang="en">
<head>
<meta charset="utf-8">
<title>Clearvale Derma – Front Label</title>
<link rel="stylesheet" href="https://fonts.googleapis.com/css2?family=Montserrat:wght@400&display=swap">
<style>
  :root {
    --backdrop: #d3d3d3;
    --label-white: #f7f7f7;
    --teal-deep: #3a9a86;
    --teal-mid: #45a891;
    --teal-light: #7cc4b1;
    --teal-glow: #86cdb9;
    --ink-green: #1f5e50;
    --gold: #d9b84e;
  }
  html, body {
    margin: 0;
    width: 1200px;
    height: 1200px;
    overflow: hidden;
    background: var(--backdrop);
    font-family: "Montserrat", sans-serif;
  }
  .label {
    position: absolute;
    left: 315px;
    top: 120px;
    width: 570px;
    height: 960px;
    background: var(--label-white);
  }
  .color-band {
    position: absolute;
    left: 0;
    top: 300px;
    width: 570px;
    height: 495px;
    background: linear-gradient(90deg, var(--teal-light), var(--teal-glow));
  }
  .band-texture {
    position: absolute;
    left: 0;
    top: 0;
    width: 570px;
    height: 120px;
    background: linear-gradient(90deg, var(--teal-mid), var(--teal-deep));
  }
  .title-panel {
    position: absolute;
    left: 55px;
    top: 117px;
    width: 460px;
    height: 378px;
    background: linear-gradient(90deg, var(--teal-light), var(--teal-glow));
  }
  .brand-name {
    position: absolute;
    left: 55px;
    top: 165px;
    width: 460px;
    margin: 0;
    text-align: center;
    font-weight: 400;
    font-size: 48px;
    line-height: 1.2;
    letter-spacing: 0.12em;
    color: var(--ink-green);
  }
  .brand-name__line { display: block; }
  .variant {
    position: absolute;
    left: 0;
    top: 395px;
    width: 570px;
    text-align: center;
  }
  .variant__name {
    display: inline-block;
    padding: 10px 0;
    border-top: 1.5px solid var(--ink-green);
    border-bottom: 1.5px solid var(--ink-green);
    font-weight: 400;
    font-size: 20px;
    letter-spacing: 0.2em;
    color: var(--ink-green);
  }
  .claim {
    position: absolute;
    left: 0;
    top: 870px;
    width: 570px;
    text-align: center;
    font-weight: 400;
    font-size: 16px;
    letter-spacing: 0.3em;
    color: var(--gold);
  }
</style>
</head>
<body>
  <div class="label">
    <div class="color-band">
      <div class="band-texture" role="img" aria-label="Subtle teal network-line texture"></div>
      <div class="title-panel"></div>
      <h1 class="brand-name">
        <span class="brand-name__line">CLEARVALE</span>
        <span class="brand-name__line">DERMA</span>
      </h1>
      <div class="variant"><span class="variant__name">SOFT MATTE GEL</span></div>
    </div>
    <div class="claim">DERMATOLOGICAL SKINCARE</div>
  </div>
</body>
</html>
```